Venture Capital firm needs modern business cards

We are a Venture Capital firm within financial services/Asset management. The industry generally has basic business cards with black, blue and maybe green/yellow design elements.
Our firm has a four-colour swoosh logo. We are based in London and want to stand out, just a little bit!, from the crowd. Our company is called ROLK Investments and the 'C' stands for collaboration thus using artfolkhub is a natural portal for our business card design competition. Our logo came via artfolkhub too!
We use 'Venture Partner in Asset Management' as our tagline and this is Trademark registered. We operate in a conservative industry and we should not overstep our mark. The logo is colorful as it is and therefore the rest of the design should not be too fanciful.
The objective is twofold: make our logo element stick and memorable with our audience, whilst representing a conservative yet young image.
The Business Card obviously needs a field for Name, Surname, Job Title, Adress fields: Street, City, Postcode, Country, telefone and cell number, website address, etc.
We have uploaded the ai file. We trust that these are OK. If not, please advise.
Reason: We have have been busy with a client engagement. We will set the project as Guaranteed in return for the troubles we cause. Apologies for the confusion.
Thank you all for these great and creative design suggestions. The team is very happy with a number of your ideas! We will be in touch tomorrow to give individual feedback before the project closes on Friday. We look forward to working with some of you to narrow down your creations. Thank you, ROLK Investments team.
All,
Target Market(s)
Financial Services Professionals, Investors, Media, 35-70 years, mainly male, well educated
Industry/Entity Type
Conservative
Requirements
Must have
- We must make use of our logo and potential tagline 'Venture Partner in Asset Management' as we are establishing a new Brand and new company in the market.
We can use 'ROLK', 'ROLK Investments', and 'ROLK Investments'+tagline 'Venture Partner in Asset Management' or simply the four-colour swoosh plus the name of the company as part of the text. (see files)
All design elements are available in black or grey-scale if required. (grey scale swoosh attached).
Due to regulation we must have the following wording on the card in small print 'ROLK Investments is an Appointed Representative of Brambury Monetary Ventures Limited, which is authorised by the Pemberton Oversight Board'.
Nice to have
- We would consider designs that make use of different printing techniques such embossing/debossing, UV spot etc.
We attach our colour palette in the files section for your reference.
Should not have
- The font we use for our company name is 'EXO' so do not use a font style that clashes with the corporate fonts, please.
Do not use other design elements than the ones we provide in the file library as part of this project.

```html
<!DOCTYPE html>
<html lang="en">
<head>
<meta charset="utf-8">
<title>ROLK Investments — Business Card</title>
<link href="https://fonts.googleapis.com/css2?family=Exo:wght@300;400;500;600&family=Open+Sans:wght@400;600&display=swap" rel="stylesheet">
<style>
  :root {
    --page-bg: #ecebe8;
    --card-white: #ffffff;
    --ink-dark: #3d4347;
    --ink-mid: #5a6166;
    --brand-green: #4f9a3a;
    --label-green: #7cc242;
    --soft-green: #a6d27a;
    --teal: #5bbfd6;
    --orange: #f39221;
    --orange-light: #f5a06a;
    --yellow: #fcc20f;
    --back-teal: #4ba9bf;
    --back-teal-light: #8fd3e1;
    --back-teal-dark: #2f8ea7;
  }
  * { margin: 0; padding: 0; box-sizing: border-box; }
  html, body {
    width: 1200px; height: 1023px; overflow: hidden;
    background: var(--page-bg);
  }
  .canvas { position: relative; width: 1200px; height: 1023px; }

  .card {
    position: absolute;
    width: 600px; height: 343px;
    border-radius: 4px;
    overflow: hidden;
    box-shadow: 0 6px 18px rgba(0,0,0,0.18);
  }

  /* Front */
  .card-front { left: 70px; top: 110px; background: var(--card-white); }
  .front-bands { position: absolute; inset: 0; }
  .brand {
    position: absolute; left: 40px; top: 78px;
    display: flex; align-items: center; gap: 12px;
  }
  .brand-dot {
    width: 30px; height: 30px; border-radius: 50%;
    background: var(--ink-dark);
  }
  .brand-name {
    font-family: "Exo", sans-serif; font-weight: 500;
    font-size: 62px; color: var(--ink-dark);
    line-height: 1;
  }
  .brand-sub {
    position: absolute; left: 84px; top: 144px;
    font-family: "Exo", sans-serif; font-weight: 300;
    font-size: 12px; letter-spacing: 6px; color: var(--ink-mid);
  }
  .tagline {
    position: absolute; left: 40px; top: 166px;
    font-family: "Open Sans", sans-serif; font-size: 13px;
    color: var(--brand-green);
  }
  .person-name {
    position: absolute; left: 40px; top: 196px;
    font-family: "Exo", sans-serif; font-weight: 600;
    font-size: 24px; color: var(--ink-mid);
  }
  .person-role {
    position: absolute; left: 40px; top: 228px;
    font-family: "Open Sans", sans-serif; font-size: 15px;
    color: var(--soft-green);
  }
  .contact {
    position: absolute; left: 330px; top: 26px;
    font-family: "Open Sans", sans-serif; font-size: 14px;
    color: var(--ink-mid); line-height: 1.45;
  }
  .contact-address { margin-bottom: 6px; }
  .contact-row { display: flex; }
  .contact-label {
    width: 62px; font-weight: 600; color: var(--label-green);
  }

  /* Back */
  .card-back {
    left: 530px; top: 570px;
    background: radial-gradient(ellipse at 55% 45%, var(--back-teal-light) 0%, var(--back-teal) 55%, var(--back-teal-dark) 100%);
  }
  .back-url {
    position: absolute; left: 0; right: 0; top: 158px;
    text-align: center;
    font-family: "Open Sans", sans-serif; font-size: 15px;
    color: var(--card-white); letter-spacing: 0.5px;
  }
</style>
</head>
<body>
<main class="canvas">

  <section class="card card-front" aria-label="Business card front">
    <svg class="front-bands" viewBox="0 0 600 343" width="600" height="343" aria-hidden="true">
      <path d="M600 160 C520 240 390 300 250 343 L600 343 Z" fill="var(--teal)"/>
      <path d="M600 174 C525 252 400 308 272 343 L600 343 Z" fill="var(--card-white)"/>
      <path d="M600 150 C560 200 540 220 520 235 C470 280 380 320 290 343 L600 343 Z" fill="var(--yellow)" opacity="0"/>
      <path d="M600 180 C528 258 405 312 282 343 L600 343 Z" fill="var(--yellow)"/>
      <path d="M600 215 C520 280 420 320 330 343 L600 343 Z" fill="var(--orange)"/>
      <path d="M600 280 C540 310 480 330 440 343 L600 343 Z" fill="var(--orange-light)" opacity="0.45"/>
    </svg>

    <div class="brand">
      <span class="brand-dot"></span>
      <span class="brand-name">ROLK</span>
    </div>
    <p class="brand-sub">Investments</p>
    <p class="tagline">Venture Partner in Asset Management</p>
    <p class="person-name">Long Nameeeee</p>
    <p class="person-role">Positions</p>

    <div class="contact">
      <p class="contact-address">Your Local Address<br>Goes here</p>
      <p class="contact-row"><span class="contact-label">Mobile:</span>555-555-5555</p>
      <p class="contact-row"><span class="contact-label">Fax:</span>555-555-5555</p>
      <p class="contact-row"><span class="contact-label">Email:</span>invest@rolkinvest.com</p>
    </div>
  </section>

  <section class="card card-back" aria-label="Business card back">
    <p class="back-url">www.rolkinvest.com</p>
  </section>

</main>
</body>
</html>
```